Guide to Internet of Things Connectivity in Social Housing

THE SIZE of the booklet is A4.
We are producing a guide to the different types of internet of things (IoT) connectivity technology in the context of UK social housing.
The guide simply explains these technologies and provides examples of where they might be relevant in social housing.
The guide need a cover and feature a different technology on each page(wifi, z-wave, Bluetooth etc). It would be great to use some graphics to bring the pages to life and communicate a sense of 'networked connectivity' if it is possible to use logos for some of these technologies without copyright issues this could be good.
Ideally the guide will fit with our current organisation branding of black and gold/yellow.
Our website is www.tallowquay.io
FOR THE INITIAL ENTRIES:
I am happy for you to do a sample of the cover/back and some internal pages but no need to do all the pages at this stage.
Social Housing sector Professionals
Internet

```html
<!DOCTYPE html>
<html lang="en">
<head>
<meta charset="utf-8">
<title>Wide Area Connections</title>
<link href="https://fonts.googleapis.com/css2?family=Montserrat:wght@400;500;700;800&display=swap" rel="stylesheet">
<style>
  :root {
    --orange: #f39a1e;
    --cream: #fdeccf;
    --ink: #2b2b2b;
    --paper: #ffffff;
  }
  html, body {
    margin: 0;
    padding: 0;
    overflow: hidden;
    background: var(--paper);
  }
  .page {
    position: relative;
    width: 851px;
    height: 1200px;
    overflow: hidden;
    background: var(--paper);
    font-family: "Montserrat", Arial, sans-serif;
    color: var(--ink);
  }
  .side-panel {
    position: absolute;
    left: 0;
    top: 62px;
    width: 410px;
    height: 1058px;
    background: var(--orange);
  }
  .section-title {
    position: absolute;
    left: 30px;
    top: 240px;
    margin: 0;
    color: var(--paper);
    font-weight: 800;
    font-size: 42px;
    line-height: 1.15;
  }
  .summary-box {
    position: absolute;
    left: 30px;
    top: 398px;
    width: 330px;
    height: 680px;
    padding: 22px 20px;
    background: var(--cream);
    box-sizing: content-box;
  }
  .summary-box p,
  .body-copy p {
    margin: 0 0 16px;
    font-size: 14px;
    line-height: 1.52;
    text-align: justify;
  }
  .summary-box strong { font-weight: 700; }
  .body-copy {
    position: absolute;
    left: 440px;
    top: 62px;
    width: 370px;
  }
  .body-copy h3 {
    margin: 4px 0 14px;
    color: var(--orange);
    font-weight: 700;
    font-size: 15px;
  }
  .page-number {
    position: absolute;
    right: 42px;
    bottom: 30px;
    color: var(--orange);
    font-weight: 500;
    font-size: 16px;
    letter-spacing: 1px;
  }
</style>
</head>
<body>
<div class="page">
  <div class="side-panel"></div>
  <h1 class="section-title">Wide Area<br>Connections</h1>

  <aside class="summary-box">
    <p><strong>Pros:</strong> Linkwell estimate that 80 per cent of UK adults have a broadband connection at home. In a housing context, this means broadband connectivity is widespread, and potentially available for an IoT implementation. Broadband is also a relatively low-cost solution.</p>
    <p><strong>Cons:</strong> 80 per cent availability is good, but not good enough for reliable implementation. The number of people with broadband will rise, but for the time being, there will still be black spots where broadband connectivity is unavailable to housing providers.</p>
    <p>Additionally, private broadband connections may not be available for IoT data transmission. The tenant may prefer that their connection is not used, or may have concerns about security and capacity. In some cases, it might be necessary to offer an incentive to the tenant in the form of benefits for keeping the device connected. Buy-in will be required for this to be a long-term option.</p>
    <p>A domestic connection is also unlikely to be under the control of the housing provider, unless it is owned, managed and paid for by them. The connection could therefore be terminated, switched off or restricted without warning, making it an impractical option for on-going data transmission as is required for IoT.</p>
  </aside>

  <section class="body-copy">
    <p>A wide area connection (WAN) is a network that transmits data over long distances. A mobile phone network is a good example of a WAN.</p>
    <p>All of the technologies in this section can transmit data over distances of several miles or more. Typically, this would be used to exchange data with the landlord via the internet.</p>
    <p>While some of these WAN technologies are widespread, many are new, and have not yet reached critical mass. Of the ones that are best known, many are typically owned and managed by tenants, making their use for IoT problematic.</p>
    <p>This section covers some of the WAN technologies you could use in an IoT implementation.</p>
    <h3>Resident Broadband connection</h3>
    <p>A broadband internet connection consists of a copper or fibre optic connection from a property to the wider internet. A router or modem sits inside the property and controls the flow of data. There are different types of broadband – cable, ADSL, fibre and more. Each individual's options will vary depending on speed requirements and local availability.</p>
  </section>

  <div class="page-number">| 04</div>
</div>
</body>
</html>
```